Church Music Album Cover

We are a Christian church in the OKC metro that is releasing a CD of songs that have connected with our congregation over the past few years. We are a church of about 1500 people of all ages- so while we want the design to be fresh, clean, and attractive- it doesn't have to be overly "youthy" or "edgy." Per the CD distribution company, the art image file you create should be able to be delivered with these requirements met:1400 x 1400 pixels minimum; 3000 x 3000 pixels maximumPNG, GIF, JPG, or JPEG file type72 - 300dpi (300dpi is the best)Less than 25mbRGB color scheme (not CMYK)
Updates

Thanks for submissions thus far. I realize my initial description may have not been the most helpful- and it some ways, I'm not 100% sure what I want. However, I would typically end to stay away from concrete images and tend to lean more towards earthy folk images. I don't even know if that makes sense. One google image search of the word "Grace" brings up individual letters spelling out Grace- each on a card clothes lined to a rope with out of focus lights or candles in the background. Another one had out of focus patio light bulbs lighting up the general text. Not sure why I like those and how they can connect to the theme, but I do. Another one had "Grace" on a pallet wall type background. Hopefully those are helpful suggestions.

Target Market(s)

Young parents- 30-40's

Colors

Requirements
Must have
• Title: Melodies from a Humble Porch
Nice to have
• Earthy/folky themes.
Should not have
• Bright colors

```html
<!DOCTYPE html>
<html lang="en">
<head>
<meta charset="utf-8">
<title>Melodies from a Humble Porch</title>
<link href="https://fonts.googleapis.com/css2?family=Alfa+Slab+One&display=swap" rel="stylesheet">
<style>
  :root {
    --wall-light: #4e8a8f;
    --wall-mid: #3a7077;
    --wall-dark: #2a545b;
    --plank-line: rgba(20, 45, 50, 0.55);
    --card: #e2c996;
    --card-edge: #c9a86c;
    --wood-letter: #f6e2b8;
    --wood-shade: #b27a3a;
    --wood-deep: #6e4520;
    --ledge-top: #4c5878;
    --ledge-bottom: #2c3450;
    --flame-glow: #f3d7a2;
  }
  * { margin: 0; padding: 0; box-sizing: border-box; }
  html, body { width: 1200px; height: 1200px; overflow: hidden; }
  body { position: relative; background: var(--wall-dark); font-family: "Alfa Slab One", Georgia, serif; }

  .wall {
    position: absolute; left: 0; top: 0; width: 1200px; height: 975px;
    background:
      repeating-linear-gradient(90deg, transparent 0 96px, var(--plank-line) 96px 99px, transparent 99px 100px),
      radial-gradient(ellipse at 50% 45%, var(--wall-light) 0%, var(--wall-mid) 55%, var(--wall-dark) 100%);
  }

  .ledge {
    position: absolute; left: 0; top: 975px; width: 1200px; height: 225px;
    background:
      radial-gradient(ellipse 90px 60px at 190px 95px, rgba(243,215,162,.45), transparent 70%),
      radial-gradient(ellipse 90px 60px at 465px 95px, rgba(243,215,162,.45), transparent 70%),
      radial-gradient(ellipse 90px 60px at 750px 95px, rgba(243,215,162,.45), transparent 70%),
      radial-gradient(ellipse 90px 60px at 1030px 95px, rgba(243,215,162,.45), transparent 70%),
      linear-gradient(180deg, var(--ledge-top), var(--ledge-bottom));
  }

  .card {
    position: absolute; display: flex; align-items: center; justify-content: center;
    background: radial-gradient(ellipse at 40% 35%, #ecd7a9, var(--card) 60%, var(--card-edge));
    box-shadow: 6px 10px 18px rgba(0, 0, 0, 0.45);
  }

  .letter {
    color: var(--wood-letter); line-height: 1;
    text-shadow:
      1px 1px 0 var(--wood-shade), 2px 2px 0 var(--wood-shade),
      3px 3px 0 var(--wood-shade), 4px 4px 0 var(--wood-deep),
      8px 10px 12px rgba(60, 30, 5, 0.5);
  }

  .title-row-one .card { width: 118px; height: 160px; top: 95px; }
  .title-row-one .letter { font-size: 84px; }

  .title-row-two .card { width: 140px; height: 200px; top: 370px; }
  .title-row-two .letter { font-size: 120px; }

  .banner {
    position: absolute; left: 190px; top: 605px; width: 830px; height: 315px;
    flex-direction: column; transform: rotate(-1deg);
    clip-path: polygon(1% 0, 99% 2%, 100% 100%, 0 98%);
  }
  .banner .letter.small { font-size: 70px; letter-spacing: 2px; }
  .banner .letter.large { font-size: 180px; letter-spacing: 4px; margin-top: 6px; }
</style>
</head>
<body>
  <div class="wall"></div>

  <div class="title-row-one" aria-label="Melodies">
    <div class="card" style="left:93px;transform:rotate(-4deg)"><span class="letter">M</span></div>
    <div class="card" style="left:221px;transform:rotate(2deg)"><span class="letter">E</span></div>
    <div class="card" style="left:349px;transform:rotate(-2deg)"><span class="letter">L</span></div>
    <div class="card" style="left:477px;transform:rotate(3deg)"><span class="letter">O</span></div>
    <div class="card" style="left:605px;transform:rotate(-3deg)"><span class="letter">D</span></div>
    <div class="card" style="left:733px;transform:rotate(2deg)"><span class="letter">I</span></div>
    <div class="card" style="left:861px;transform:rotate(-2deg)"><span class="letter">E</span></div>
    <div class="card" style="left:989px;transform:rotate(5deg)"><span class="letter">S</span></div>
  </div>

  <div class="title-row-two" aria-label="from">
    <div class="card" style="left:299px;transform:rotate(4deg)"><span class="letter">F</span></div>
    <div class="card" style="left:453px;transform:rotate(-1deg)"><span class="letter">R</span></div>
    <div class="card" style="left:607px;transform:rotate(3deg)"><span class="letter">O</span></div>
    <div class="card" style="left:761px;transform:rotate(-4deg)"><span class="letter">M</span></div>
  </div>

  <div class="card banner">
    <span class="letter small">A HUMBLE</span>
    <span class="letter large">PORCH</span>
  </div>

  <div class="ledge" role="img" aria-label="Row of four lit tealight candles on a blue wooden ledge"></div>
</body>
</html>
```